Store Front / Boutique Front window signage

I am looking to have a sign printed to stick on the glass of my new Kitchens Cabinets showroom. I already have a logo that I will include however this is the "Boutique" location so I am looking to have my logo incorporated for brand recognition but I do not want just my logo. I want something classy, minimalist with class. Maybe even old school or vintage in style. I will include my store front window sizes and a picture of the store front.

My thought is to take my logo small to moderate in size. Take away the "Cabinetry and Design" part and place that statement larger like this
"Cabinetry and Design Boutique"
My website is Brambleforthkitchens.com
window panes are as follows
left is 72 3/4" wide
right is 70" wide
height is 97 1/2"

I would like to see something not too large , across the two panes
Updates

I have been with work family , looking to choose the best created design and then modify to my liking

Target Market(s)

People !

Font styles to use
Decorative
Script
Other font styles liked:
• vintage , classic

Requirements
Must have
• Tasteful . Maybe logo and small strip along the bottom with a manufacturers logos.
Should not have
• Should not be too large, the signage is not intended to be seen from driving by , more for foot traffic

```html
<!DOCTYPE html>
<html lang="en">
<head>
<meta charset="utf-8">
<title>Brambleforth Kitchens – Boutique Window Signage</title>
<link href="https://fonts.googleapis.com/css2?family=Cinzel:wght@500;700&display=swap" rel="stylesheet">
<style>
  :root {
    --glass: #2b2b2e;
    --gold: #f0c232;
    --gold-soft: #d9a928;
  }
  html, body {
    margin: 0;
    padding: 0;
    width: 1200px;
    height: 1200px;
    overflow: hidden;
    background: var(--glass);
  }
  .signage {
    position: relative;
    width: 1200px;
    height: 1200px;
    background: var(--glass);
    font-family: "Cinzel", serif;
    color: var(--gold);
  }
  .frame {
    position: absolute;
    left: 50px;
    top: 230px;
    width: 1100px;
    height: 740px;
  }
  .frame svg.frame-lines {
    position: absolute;
    inset: 0;
  }
  .corner-flourish {
    position: absolute;
    width: 62px;
    height: 62px;
    background: var(--gold-soft);
    opacity: 0.85;
    border-radius: 4px;
  }
  .corner-flourish.tl { left: -4px; top: -4px; }
  .corner-flourish.tr { right: -4px; top: -4px; }
  .corner-flourish.bl { left: -4px; bottom: -4px; }
  .corner-flourish.br { right: -4px; bottom: -4px; }

  .panel {
    position: absolute;
    top: 0;
    width: 520px;
    height: 740px;
    text-align: center;
  }
  .panel.left { left: 40px; }
  .panel.right { left: 582px; }

  .brand-name {
    position: absolute;
    top: 318px;
    left: 0;
    width: 100%;
    font-weight: 700;
    font-size: 38px;
    line-height: 1.05;
    letter-spacing: 3px;
    text-transform: uppercase;
    color: var(--gold);
  }
  .tagline {
    position: absolute;
    top: 322px;
    left: 0;
    width: 100%;
    font-weight: 500;
    font-size: 28px;
    line-height: 1.1;
    letter-spacing: 2.5px;
    text-transform: uppercase;
  }
  .divider {
    position: absolute;
    top: 398px;
    left: 110px;
    width: 300px;
    height: 20px;
  }
  .website {
    position: absolute;
    top: 660px;
    left: 0;
    width: 100%;
    font-weight: 500;
    font-size: 15px;
    letter-spacing: 0.5px;
    text-transform: uppercase;
  }
</style>
</head>
<body>
<main class="signage">
  <section class="frame">
    <svg class="frame-lines" width="1100" height="740" viewBox="0 0 1100 740" aria-hidden="true">
      <rect x="4" y="4" width="1092" height="732" rx="14" fill="none" stroke="var(--gold)" stroke-width="5"/>
      <rect x="26" y="24" width="1048" height="692" rx="10" fill="none" stroke="var(--gold)" stroke-width="2"/>
    </svg>
    <div class="corner-flourish tl" role="img" aria-label="Gold scroll flourish, top left corner"></div>
    <div class="corner-flourish tr" role="img" aria-label="Gold scroll flourish, top right corner"></div>
    <div class="corner-flourish bl" role="img" aria-label="Gold scroll flourish, bottom left corner"></div>
    <div class="corner-flourish br" role="img" aria-label="Gold scroll flourish, bottom right corner"></div>

    <div class="panel left">
      <div class="brand-name">Brambleforth<br>Kitchens</div>
      <svg class="divider" viewBox="0 0 300 20" aria-hidden="true">
        <line x1="0" y1="10" x2="128" y2="10" stroke="var(--gold)" stroke-width="1.5"/>
        <line x1="172" y1="10" x2="300" y2="10" stroke="var(--gold)" stroke-width="1.5"/>
        <ellipse cx="150" cy="10" rx="14" ry="8" fill="var(--gold)" role="img" aria-label="Small gold centre ornament"/>
      </svg>
      <div class="website">Brambleforthkitchens.com</div>
    </div>

    <div class="panel right">
      <div class="tagline">Cabinetry and<br>Design Boutique</div>
      <svg class="divider" viewBox="0 0 300 20" aria-hidden="true">
        <line x1="0" y1="10" x2="128" y2="10" stroke="var(--gold)" stroke-width="1.5"/>
        <line x1="172" y1="10" x2="300" y2="10" stroke="var(--gold)" stroke-width="1.5"/>
        <ellipse cx="150" cy="10" rx="14" ry="8" fill="var(--gold)" role="img" aria-label="Small gold centre ornament"/>
      </svg>
      <div class="website">Brambleforthkitchens.com</div>
    </div>
  </section>
</main>
</body>
</html>
```